Brisbane IT support business needs our first letterhead (Contest)

Hello we are a Brisbane based Information Technology company providing support and services to small and medium sized businesses. We provide a range of services and solutions.

The business name is Kestrel Data Network Systems, or KDNS for short.

I am looking for a letterhead that looks professional (don't we all want that), but most importantly, it most utilize the colours in the logo attached, and any text used preferably in font type: HandelGotDBol.

```html
<!DOCTYPE html>
<html lang="en">
<head>
<meta charset="utf-8">
<title>KDNS Stationery – Folder and Letterhead</title>
<link rel="stylesheet" href="https://fonts.googleapis.com/css2?family=Aldrich&display=swap">
<style>
  :root {
    --backdrop: #000000;
    --navy: #03465f;
    --orange: #ea7f26;
    --paper: #ffffff;
    --mist: #eef1f3;
    --ink: #03465f;
  }
  * { margin: 0; padding: 0; box-sizing: border-box; }
  html, body { width: 1200px; height: 862px; overflow: hidden; background: var(--backdrop); }
  body { position: relative; font-family: "Aldrich", "Arial", sans-serif; }

  .sheet { position: absolute; top: 32px; width: 561px; height: 793px; overflow: hidden; }

  /* Folder cover */
  .cover { left: 30px; background: var(--navy); }
  .cover .divider-white { position: absolute; left: 0; top: 731px; width: 100%; height: 9px; background: var(--paper); }
  .cover .band-orange { position: absolute; left: 0; top: 740px; width: 100%; height: 53px; background: var(--orange); }
  .cover .brand { position: absolute; left: 131px; top: 268px; display: flex; align-items: center; gap: 26px; }
  .cover .brand-dot { width: 108px; height: 108px; border-radius: 50%; background: var(--paper); }
  .cover .brand-name { font-size: 64px; line-height: 1; color: var(--orange); letter-spacing: 1px; }

  /* Letterhead */
  .letterhead { left: 614px; background: var(--paper); }
  .letterhead .brand { position: absolute; left: 24px; top: 27px; display: flex; align-items: center; gap: 14px; }
  .letterhead .brand-dot { width: 58px; height: 58px; border-radius: 50%; background: var(--navy); }
  .letterhead .brand-name { font-size: 31px; line-height: 1; color: var(--orange); letter-spacing: 0.5px; }

  .contact { position: absolute; left: 407px; top: 20px; list-style: none; }
  .contact li { display: flex; align-items: center; height: 21px; font-size: 11px; color: var(--orange); white-space: nowrap; }
  .contact li.phone { height: 25px; font-size: 12px; }
  .contact svg { width: 16px; height: 18px; margin-right: 9px; fill: var(--navy); flex: none; }

  .footer-info { position: absolute; left: 23px; top: 652px; width: 250px; color: var(--ink); }
  .footer-info .company { font-size: 11px; line-height: 14px; color: var(--orange); margin-bottom: 3px; }
  .footer-info .address { font-size: 8.6px; line-height: 11.5px; }
  .footer-info .address-label { font-size: 10px; color: var(--orange); margin-right: 8px; }

  .skyline-fade { position: absolute; left: 316px; top: 660px; width: 245px; height: 71px;
    background: linear-gradient(to top, var(--mist), rgba(238,241,243,0)); }

  .letterhead .band-orange { position: absolute; left: 0; top: 731px; width: 100%; height: 9px; background: var(--orange); }
  .letterhead .band-navy { position: absolute; left: 0; top: 740px; width: 100%; height: 53px; background: var(--navy); }
</style>
</head>
<body>

  <section class="sheet cover" aria-label="Folder cover">
    <div class="brand">
      <div class="brand-dot"></div>
      <div class="brand-name">KDNS</div>
    </div>
    <div class="divider-white"></div>
    <div class="band-orange"></div>
  </section>

  <section class="sheet letterhead" aria-label="Letterhead">
    <div class="brand">
      <div class="brand-dot"></div>
      <div class="brand-name">KDNS</div>
    </div>

    <ul class="contact">
      <li class="phone">
        <svg viewBox="0 0 16 18" aria-hidden="true"><rect x="3" y="0" width="10" height="18" rx="2"/><rect x="4.5" y="2" width="7" height="12" fill="#fff"/><circle cx="8" cy="16" r="0.9" fill="#fff"/></svg>
        555 - 014 - 372
      </li>
      <li class="phone">
        <svg viewBox="0 0 16 18" aria-hidden="true"><rect x="4" y="3" width="8" height="5"/><rect x="1" y="7" width="14" height="7" rx="1.5"/><rect x="4" y="11" width="8" height="5" fill="#fff" stroke="#03465f" stroke-width="1"/></svg>
        555 - 014 - 372
      </li>
      <li>
        <svg viewBox="0 0 16 18" aria-hidden="true"><rect x="1" y="5" width="14" height="9"/><path d="M1.5 5.5 L8 10.5 L14.5 5.5" fill="none" stroke="#fff" stroke-width="1.2"/></svg>
        hi@kdnsmail.com
      </li>
    </ul>

    <div class="skyline-fade" role="img" aria-label="Faint city skyline silhouette"></div>

    <div class="footer-info">
      <p class="company">Kestrel Data Network Systems</p>
      <p class="address"><span class="address-label">Address:</span>Lorem Ipsum is simply dummy text of the printing and typesetting industry. Lorem Ipsum has been the industry's standard dummy text ever since the 1500s,</p>
    </div>

    <div class="band-orange"></div>
    <div class="band-navy"></div>
  </section>

</body>
</html>
```